STORMLYNX BUSINESS CARDS REDESIGN

We updated our logo and now need to bring fresh new life into the company business cards incorporating the new logo.

www.stormlynxguard.example - website for reference

Industry/Entity Type

Business

Contact Information for Business Card

SEE SHEET WITH DETAILS NOTED

```html
<!DOCTYPE html>
<html lang="en">
<head>
<meta charset="utf-8">
<title>StormLynx Business Card</title>
<link rel="stylesheet" href="https://fonts.googleapis.com/css2?family=Roboto+Condensed:wght@700&family=Montserrat:wght@600&display=swap">
<style>
  :root {
    --page: #eeeae4;
    --white: #ffffff;
    --orange: #f6a01a;
    --orange-deep: #ee6a1c;
    --red: #c4262b;
    --red-dark: #a31e23;
    --ink: #333333;
    --label: #d3281f;
    --gold: #d9a81e;
    --grey: #8c8c8c;
    --black: #111111;
  }
  * { box-sizing: border-box; margin: 0; padding: 0; }
  html, body { width: 1100px; height: 1200px; overflow: hidden; }
  body { background: var(--page); position: relative; font-family: "Roboto Condensed", "Arial Narrow", sans-serif; font-weight: 700; }
  .card { position: absolute; left: 70px; width: 960px; height: 545px; background: var(--white); overflow: hidden; box-shadow: 0 4px 14px rgba(0,0,0,.18); }
  .card--front { top: 40px; }
  .card--back { top: 615px; }

  /* front */
  .brand { position: absolute; left: 74px; top: 56px; width: 280px; height: 320px; display: flex; flex-direction: column; align-items: center; justify-content: center; gap: 18px; }
  .brand__dot { width: 120px; height: 120px; border-radius: 50%; background: var(--orange-deep); }
  .brand__name { font-size: 46px; color: var(--red); letter-spacing: 1px; }
  .divider { position: absolute; left: 427px; top: 104px; width: 3px; height: 280px; background: linear-gradient(to bottom, #d8d8d8, #b8b8b8, #d8d8d8); }
  .person { position: absolute; left: 470px; top: 100px; }
  .person__name { font-size: 37px; color: var(--red); line-height: 1; }
  .person__role { font-size: 24px; color: var(--orange); margin-top: 8px; }
  .contacts { position: absolute; left: 470px; top: 190px; list-style: none; font-size: 26px; line-height: 34.5px; color: var(--ink); }
  .contacts__label { color: var(--label); }
  .swoosh { position: absolute; left: 0; bottom: 0; width: 960px; height: 180px; }
  .website { position: absolute; left: 83px; top: 480px; font-size: 24px; color: var(--white); }
  .seal { position: absolute; left: 760px; top: 398px; width: 124px; height: 124px; border-radius: 50%; background: radial-gradient(circle, #f3d46a, var(--gold)); border: 4px solid #b88b12; }

  /* back */
  .card--back .panel { position: absolute; left: 0; top: 0; width: 960px; height: 346px; background: linear-gradient(90deg, var(--orange) 0%, var(--orange-deep) 45%, var(--red) 100%); }
  .headline { position: absolute; top: 44px; width: 100%; text-align: center; color: var(--white); font-size: 46px; line-height: 56px; }
  .services { position: absolute; top: 186px; left: 56px; display: grid; grid-template-columns: 424px 420px; row-gap: 10px; list-style: none; color: var(--white); font-size: 30px; line-height: 36px; }
  .services li { display: flex; align-items: center; gap: 10px; }
  .services svg { width: 24px; height: 24px; flex: none; }
  .licence { position: absolute; top: 346px; left: 0; width: 960px; height: 67px; background: var(--black); color: var(--white); font-family: "Montserrat", Arial, sans-serif; font-weight: 600; font-size: 23px; display: flex; align-items: center; justify-content: center; }
  .partners { position: absolute; top: 430px; left: 0; width: 960px; height: 110px; }
  .partner { position: absolute; }
  .partner--wide { left: 158px; top: 26px; width: 160px; height: 62px; border-radius: 8px; background: #23408e; }
  .partner--square { left: 388px; top: 18px; width: 72px; height: 80px; border: 5px solid var(--black); background: var(--white); }
  .partner--round { left: 566px; top: 14px; width: 88px; height: 88px; border-radius: 50%; border: 2px solid #bbbbbb; background: #f4f4f4; }
  .partner--shield { left: 720px; top: 12px; width: 80px; height: 92px; border-radius: 10px 10px 40px 40px; background: var(--red-dark); }
</style>
</head>
<body>

<section class="card card--front">
  <div class="brand">
    <div class="brand__dot"></div>
    <div class="brand__name">STORMLYNX</div>
  </div>
  <div class="divider"></div>
  <div class="person">
    <div class="person__name">MARCUS HALE</div>
    <div class="person__role">Position</div>
  </div>
  <ul class="contacts">
    <li><span class="contacts__label">Cell:</span> 1-888-888-8888</li>
    <li><span class="contacts__label">Office:</span> 1-555-010-4420</li>
    <li><span class="contacts__label">Toll Free:</span> 1-800-STORMLYNX</li>
    <li><span class="contacts__label">Fax:</span> 1-888-888-8888</li>
    <li><span class="contacts__label">E-mail:</span> name@stormlynxguard.example</li>
  </ul>
  <svg class="swoosh" viewBox="0 0 960 180" preserveAspectRatio="none" aria-hidden="true">
    <defs>
      <linearGradient id="sweep" x1="0" x2="1" y1="0" y2="0">
        <stop offset="0" stop-color="#f6a01a"/>
        <stop offset=".45" stop-color="#ef6f1d"/>
        <stop offset="1" stop-color="#c4262b"/>
      </linearGradient>
    </defs>
    <path d="M0 60 C 180 0, 420 20, 620 80 C 760 120, 880 60, 960 0 L960 180 L0 180 Z" fill="url(#sweep)"/>
    <path d="M0 58 C 180 -2, 420 18, 620 78 C 760 118, 880 58, 960 -2" fill="none" stroke="#ffffff" stroke-width="14"/>
    <path d="M30 52 C 200 4, 420 26, 620 84 C 760 122, 880 66, 960 8" fill="none" stroke="#8c8c8c" stroke-width="5"/>
  </svg>
  <div class="website">www.stormlynxguard.example</div>
  <div class="seal" role="img" aria-label="Anniversary seal"></div>
</section>

<section class="card card--back">
  <div class="panel"></div>
  <h1 class="headline">ONE-STOP SAFETY-SHOP<br>24-HOUR EMERGENCY SERVICE</h1>
  <ul class="services">
    <li><svg viewBox="0 0 24 24"><path d="M3 13 L9 19 L21 5" fill="none" stroke="#fff" stroke-width="3"/></svg>Fire Sprinkler Systems</li>
    <li><svg viewBox="0 0 24 24"><path d="M3 13 L9 19 L21 5" fill="none" stroke="#fff" stroke-width="3"/></svg>First-Aid Supplies</li>
    <li><svg viewBox="0 0 24 24"><path d="M3 13 L9 19 L21 5" fill="none" stroke="#fff" stroke-width="3"/></svg>Fire Extinguishers</li>
    <li><svg viewBox="0 0 24 24"><path d="M3 13 L9 19 L21 5" fill="none" stroke="#fff" stroke-width="3"/></svg>Fire Safety / Training Classes</li>
    <li><svg viewBox="0 0 24 24"><path d="M3 13 L9 19 L21 5" fill="none" stroke="#fff" stroke-width="3"/></svg>Fire Suppression Systems</li>
    <li><svg viewBox="0 0 24 24"><path d="M3 13 L9 19 L21 5" fill="none" stroke="#fff" stroke-width="3"/></svg>Fire Hose Sales &amp; Service</li>
  </ul>
  <div class="licence">CA State C16 # 402817&nbsp;&nbsp;State Fire Marshal # 5623</div>
  <div class="partners">
    <div class="partner partner--wide" role="img" aria-label="Partner association badge"></div>
    <div class="partner partner--square" role="img" aria-label="Partner association badge"></div>
    <div class="partner partner--round" role="img" aria-label="Partner association badge"></div>
    <div class="partner partner--shield" role="img" aria-label="Partner agency badge"></div>
  </div>
</section>

</body>
</html>
```